GlimmerFrocks.com Banner AD

We are looking for some talented creators to create for us a banner ad for our online clothing store that specializes in dresses. We are looking for a fresh, clean, and sleek LUMA, P&Q, and Plume appeal- clean, modern and sophisticated.

We would like for the final project to appear professionally done, we've had projects completed by several talent out there that did not capture our image, and let's just say it was too cluttered and appeared as if a high school editor had completed it.

I have attached a few files for you to reference, I have File 1, 2, 3, 8 and the P&Q photos as examples of what we DO like.

I have attached File 5, which is the work of one the designers that was working on this project. Although it is very simple and gets the point across, it doesn't come across like a magazine editorial.

I have attached File 6, that is the main photo we wish to use for our banner.

I have attached File 7, which is what a creator had done for us via Taskfern.com, that is a good example of what we do NOT want.

That is about sums it up! I hope the examples are useful tools for you!
Updates

Hi Designers!

Thank you so much for your submissions! I enjoy viewing each and every one of them! Please view my update on what I am looking for, I have made some adjustments and have added a few more examples to reference, I have made my direction a bit more clearer. Because it seems some designers are not quite understanding my direction. I know you all have amazing talent and I am hoping to see something I am looking for and I love soon! If you have any other questions, please don't hesitate to ask! 

Target Market(s)

Our company targets women of all ages, we carry dresses that cater to every occasion, whether its an older woman looking for a dress to attend a wedding or a teenager looking for a prom dress. We want our front page banner to appear fresh, clean, with a feminine touch, we want to stray from tacky (gradients, etc..) and keep it classy all while maintaining that magazine editorial element, we want to be more fashion focused, like Plume. We want this project to appear professionally done. Our desired concept is something out of a magazine editorial, not too much going on, while shifting focus more on the dress itself than a design element like flowers or spring backgrounds.

Industry/Entity Type

High School

Requirements
Must have
• We want a plume fashion appeal, magazine editorial type of look. The phrases below should be included"

"New Season New Sexy Dresses"

"Free U.S shipping on orders $75+"
"Shop our sales up to 60% off"

All of the other phrases do not need to be included. Also, Do not include the parenthesis.
Should not have
• Only include the photo I've attached that appears solo. Please do not include the other 3 dresses that is displayed in a banner that was created for us by another designer. (that is provided as an example only)

```html
<!DOCTYPE html>
<html lang="en">
<head>
<meta charset="utf-8">
<title>GlimmerFrocks.com — New Season Sale Banner</title>
<link rel="stylesheet" href="https://fonts.googleapis.com/css2?family=Tinos:ital,wght@0,400;0,700;1,400&family=Poppins:wght@500&display=swap">
<style>
  :root {
    --paper: #ffffff;
    --ink: #111111;
    --magenta: #e3166f;
    --sky-blue: #2f9bd8;
    --photo-tone: #6f625c;
    --bloom-tint: #fbe4ee;
  }
  * { margin: 0; padding: 0; box-sizing: border-box; }
  html, body { width: 1200px; height: 1043px; overflow: hidden; background: var(--paper); }
  .banner {
    position: relative;
    width: 1200px;
    height: 1043px;
    overflow: hidden;
    background: var(--paper);
  }
  .headline {
    position: absolute;
    left: 100px;
    top: 57px;
    font-family: "Tinos", "Times New Roman", serif;
    font-weight: 400;
    font-size: 145px;
    line-height: 1;
    letter-spacing: 1px;
    color: var(--ink);
    white-space: nowrap;
  }
  .subhead {
    position: absolute;
    right: 110px;
    top: 202px;
    font-family: "Tinos", "Times New Roman", serif;
    font-style: italic;
    font-weight: 400;
    font-size: 111px;
    line-height: 1;
    color: var(--magenta);
    white-space: nowrap;
  }
  .shipping {
    position: absolute;
    right: 57px;
    top: 339px;
    font-family: "Tinos", "Times New Roman", serif;
    font-weight: 700;
    font-size: 43px;
    line-height: 1;
    color: var(--sky-blue);
    white-space: nowrap;
  }
  .sale {
    position: absolute;
    left: 62px;
    top: 417px;
    font-family: "Poppins", "Arial", sans-serif;
    font-weight: 500;
    font-size: 170px;
    line-height: 174px;
    letter-spacing: 2px;
    color: var(--ink);
  }
  .sale span { display: block; }
  .models-photo {
    position: absolute;
    left: 505px;
    top: 405px;
    width: 590px;
    height: 525px;
    background: var(--photo-tone);
  }
  .bloom {
    position: absolute;
    background: var(--bloom-tint);
  }
  .bloom--left {
    left: 0;
    top: 960px;
    width: 700px;
    height: 83px;
  }
  .bloom--right {
    left: 1110px;
    top: 620px;
    width: 90px;
    height: 423px;
  }
</style>
</head>
<body>
  <main class="banner">
    <div class="bloom bloom--left" role="img" aria-label="Pink floral swirl and butterfly ornament"></div>
    <div class="bloom bloom--right" role="img" aria-label="Pink flowers and butterfly ornament"></div>
    <h1 class="headline">NEW SEASON</h1>
    <p class="subhead">New Sexy Dresses</p>
    <p class="shipping">Free U.S shipping on orders $75+</p>
    <div class="models-photo" role="img" aria-label="Photo of five women in fashionable outfits standing side by side"></div>
    <p class="sale"><span>SALE</span><span>60%</span><span>OFF</span></p>
  </main>
</body>
</html>
```